International Freight Forwarder need a business card

We need a logo design for a freight forwarding company . We are active in Sea Transportation, Truck transportation, and Air Transportation, The design should be have normal dimensions of a card and should not have cuts and holes in its design (printed design is required - lamination accepted)

The said company is agent and sales representative of 2 other Shipping companies (whose logos, name, and website should also be mentioned on the card)

Industry/Entity Type

Logistics

Contact Information for Business Card

Address is "No.7, 2nd Sarv Baghestan-e-Nouri, Tehran, IR
Tel number is +98 21 66394512
Fax number is +98 21 66395830
E-Mail address is info@roshanbarsaz.com
Website is www.roshanbarsaz.com

Open Layer Logos attached as well

Colors
33a6d7
0292cd
0255a3
3276b5
85abd2
85cae6
cee9f5
d5e2ee
ffffff

Requirements
Must have
• Main logo of Roshan Barsaz
• Logo of TQM Shipping Line
• London, United Kingdom
• tqmline.com
• Logo of Calm Reef Shipping
• Dubai, United Arab Emirates
• crsuae.com
• We require OPEN layer file to be submitted to us upon project selection.
Should not have
• Weird Designs such as cuts to the shape or holes in design.

```html
<!DOCTYPE html>
<html lang="en">
<head>
<meta charset="utf-8">
<title>Roshan Barsaz – Business Card</title>
<link rel="stylesheet" href="https://fonts.googleapis.com/css2?family=Open+Sans:wght@400;600;700&display=swap">
<style>
  :root {
    --sky: #33a6d7;
    --azure: #0292cd;
    --navy: #0255a3;
    --steel: #3276b5;
    --mist: #85abd2;
    --ice: #cee9f5;
    --paper: #ffffff;
    --ink: #4a4a4a;
    --stage: #e6e9ed;
  }
  * { box-sizing: border-box; margin: 0; padding: 0; }
  html, body {
    width: 1200px; height: 960px; overflow: hidden;
    background: var(--stage);
    font-family: "Open Sans", Arial, sans-serif;
  }
  .canvas {
    width: 1200px; height: 960px;
    display: flex; flex-direction: column; align-items: center; justify-content: center; gap: 48px;
  }
  .card {
    position: relative;
    width: 740px; height: 423px;
    background: var(--paper);
    box-shadow: 0 2px 10px rgba(0,0,0,.12);
    overflow: hidden;
  }

  /* Back side */
  .card-back .agent {
    position: absolute; left: 60px; top: 70px; width: 220px;
    display: flex; flex-direction: column; align-items: center; text-align: center; gap: 12px;
  }
  .agent-mark {
    width: 96px; height: 96px; border-radius: 50%;
    background: var(--ice);
  }
  .agent-name {
    color: var(--steel); font-size: 14px; font-weight: 600; line-height: 1.3;
  }
  .divider {
    position: absolute; left: 330px; top: 60px; width: 1px; height: 200px;
    background: var(--mist);
  }
  .partners {
    position: absolute; left: 370px; top: 80px;
    display: flex; flex-direction: column; gap: 46px;
  }
  .partner { display: flex; align-items: center; gap: 14px; }
  .partner-mark { width: 48px; height: 48px; border-radius: 50%; }
  .partner-mark.sky { background: var(--sky); }
  .partner-mark.navy { background: var(--navy); }
  .partner-name { font-size: 16px; font-weight: 700; }
  .partner-name.sky { color: var(--sky); }
  .partner-name.navy { color: var(--navy); }
  .offices {
    position: absolute; right: 40px; top: 300px;
    border-top: 1.5px solid var(--steel);
    padding-top: 4px;
    color: var(--ink); font-size: 15px; line-height: 1.45; text-align: right;
  }

  /* Front side */
  .card-front .accent {
    position: absolute; left: 0; top: 78px; width: 10px; height: 34px;
    background: var(--navy);
  }
  .identity { position: absolute; left: 40px; top: 74px; }
  .person-name { color: var(--navy); font-size: 19px; font-weight: 700; letter-spacing: .3px; }
  .person-role { color: var(--steel); font-size: 17px; }
  .contact {
    position: absolute; left: 40px; top: 150px;
    list-style: none; color: var(--ink); font-size: 15px; line-height: 1.55;
  }
  .contact li { display: flex; align-items: center; gap: 10px; }
  .contact .address { display: block; padding-left: 0; margin-bottom: 2px; }
  .contact svg { width: 13px; height: 13px; fill: var(--navy); flex: none; }
  .brand-sign {
    position: absolute; right: 56px; bottom: 70px;
    color: var(--steel); font-size: 42px; font-weight: 700;
    display: flex; align-items: center; gap: 18px;
  }
  .brand-sign .dot { width: 40px; height: 40px; background: var(--sky); border-radius: 50%; }
</style>
</head>
<body>
<main class="canvas">

  <section class="card card-back" aria-label="Card back">
    <div class="agent">
      <span class="agent-mark"></span>
      <p class="agent-name">Roshan Barsaz<br>International<br>Transport.Co L.L.c</p>
    </div>
    <span class="divider"></span>
    <div class="partners">
      <div class="partner">
        <span class="partner-mark sky"></span>
        <span class="partner-name sky">TQM Shipping Line Ltd</span>
      </div>
      <div class="partner">
        <span class="partner-mark navy"></span>
        <span class="partner-name navy">Calm Reef Shipping LLC</span>
      </div>
    </div>
    <p class="offices">
      TQM Shipping Line London, United Kingdom | tqmline.com<br>
      Calm Reef Shipping Dubai, United Arab Emirates | crsuae.com
    </p>
  </section>

  <section class="card card-front" aria-label="Card front">
    <span class="accent"></span>
    <div class="identity">
      <p class="person-name">DANIEL CARTER</p>
      <p class="person-role">CEO/FOUNDER</p>
    </div>
    <ul class="contact">
      <li class="address">No.7, 2nd Sarv<br>Baghestan-e-Nouri, Tehran, IR</li>
      <li><svg viewBox="0 0 16 16" aria-hidden="true"><path d="M3 1h3l1.5 4-2 1.3a9 9 0 0 0 4.2 4.2L11 8.5l4 1.5v3a2 2 0 0 1-2 2A12 12 0 0 1 1 3a2 2 0 0 1 2-2z"/></svg>+98 21 66394512</li>
      <li><svg viewBox="0 0 16 16" aria-hidden="true"><path d="M4 1h7v4H4zM1 6h14v7h-3v2H4v-2H1zm4 5v3h6v-3z"/></svg>+98 21 66395830</li>
      <li><svg viewBox="0 0 16 16" aria-hidden="true"><path d="M1 3h14v10H1zm1.5 1.2L8 8.5l5.5-4.3z"/></svg>info@roshanbarsaz.com</li>
      <li><svg viewBox="0 0 16 16" aria-hidden="true"><circle cx="8" cy="8" r="7"/></svg>www.roshanbarsaz.com</li>
    </ul>
    <div class="brand-sign"><span class="dot"></span>Roshan Barsaz</div>
  </section>

</main>
</body>
</html>
```